Solvaro Cantina Menu

We are looking to take a menu from excel for our new Mexican Restaurant and turn into into a classy menu that can be printed or used with a QR code link. We are located in Hawaii. We would like an easy-to-read and not over-the-top Mexican style. Elevated Mexican | Fresh Mexican We need to be able to make edits for price changes. Logo and excel spreadsheet attached.
Any colors to match our logo and mood board. Please no stock gifs and cactus...

Food on 1 page and drinks on separate pages.

```html
<!DOCTYPE html>
<html lang="en">
<head>
<meta charset="utf-8">
<title>Solvaro Cantina Menu</title>
<link href="https://fonts.googleapis.com/css2?family=Oswald:wght@400;500&family=Alegreya+Sans:wght@400;500;700&family=Arvo:wght@400;700&family=Monsieur+La+Doulaise&family=Fjalla+One&display=swap" rel="stylesheet">
<style>
:root{
  --backdrop:#d9dadd;
  --paper:#efeeeb;
  --rust:#a6482a;
  --blue:#3f7fb5;
  --blue-soft:#6fa5d4;
  --blue-deep:#2d6194;
  --blue-mid:#3e7bb0;
  --ink:#1f1f1f;
  --ink-soft:#333;
  --on-blue:#eef3f8;
  --frame:#9cbfe0;
}
*{box-sizing:border-box;margin:0;padding:0}
html,body{width:1200px;height:1008px;overflow:hidden;background:var(--backdrop)}
body{font-family:"Alegreya Sans",sans-serif;color:var(--ink)}
.menu{position:absolute;left:0;top:111px;width:1200px;height:786px;display:flex}
.panel{position:relative;width:400px;height:786px;background:var(--paper)}
.panel--specials{background:linear-gradient(200deg,var(--blue-mid) 0%,#4f8ac0 28%,var(--blue-deep) 100%);color:var(--on-blue)}
.framed{position:absolute;border:1.5px solid var(--frame)}
.panel--specials .framed{border-color:rgba(230,240,250,.45)}

.section-title{font-family:"Fjalla One",sans-serif;text-align:center;line-height:1;letter-spacing:-.5px}
.section-sub{font-family:"Oswald",sans-serif;font-size:10px;letter-spacing:1px;text-align:center;text-transform:uppercase}

.item{margin-bottom:3px}
.item-head{display:flex;justify-content:space-between;font-family:"Oswald",sans-serif;font-weight:400;font-size:12px;line-height:14px;text-transform:uppercase;letter-spacing:.1px}
.desc{font-size:11px;line-height:12.4px;padding-left:11px;color:var(--ink-soft)}
.opt{display:flex;justify-content:space-between;padding-left:11px;font-family:"Oswald",sans-serif;font-size:11px;line-height:14px;text-transform:uppercase;font-weight:500}
.price{font-family:"Alegreya Sans",sans-serif;font-weight:500;font-size:11px}

/* appetizers */
.appetizers{left:25px;top:25px;width:352px;height:392px}
.appetizers .section-title{color:var(--rust);font-size:36px;margin-top:14px}
.appetizers .section-sub{color:var(--rust);margin-bottom:6px}
.appetizers .list{padding:0 33px 0 18px}
.appetizers .item-head{color:var(--rust)}
.appetizers .opt{color:var(--ink)}

.soup-salad{left:25px;top:449px;width:352px;height:283px}
.band{height:26px;background:var(--blue-soft);color:#fff;font-family:"Oswald",sans-serif;font-size:14px;text-align:center;line-height:26px;letter-spacing:.3px;text-transform:uppercase}
.dish-title{font-family:"Oswald",sans-serif;color:var(--blue);font-size:14px;line-height:15px;text-transform:uppercase}
.soup-salad .cols{display:flex;gap:10px;padding:14px 12px 0 18px}
.soup-col{width:186px;position:relative}
.salad-col{width:124px}
.small-text{font-size:10.5px;line-height:12px;color:var(--ink-soft)}
.soup-text{width:110px;margin-top:3px}
.soup-art{position:absolute;left:116px;top:34px;width:66px;height:56px;border-radius:8px 8px 30px 30px;background:#c98f6a;opacity:.75}
.sizes{margin-top:8px;padding-left:10px;font-family:"Oswald",sans-serif;font-size:11px;line-height:15px}
.sizes div{display:flex;width:90px;justify-content:space-between}
.sizes span:last-child{font-family:"Alegreya Sans",sans-serif}
.salad-price{font-size:11px;margin:4px 0 2px}
.suprema{padding:4px 33px 0 18px}
.suprema .small-text{margin:4px 0 4px}

/* specials */
.specials{left:25px;top:25px;width:338px;height:737px}
.specials .section-title{font-size:36px;margin-top:17px;color:#f2f5f8}
.specials .section-sub{margin-bottom:6px}
.specials .list{padding:0 10px 0 18px}
.specials .desc{color:#dbe6f1;font-size:10.7px;line-height:12.6px}
.specials .opt{font-size:9.5px;line-height:12.6px}
.specials .opt .price{font-size:9.5px}
.specials .item{margin-bottom:2px}

/* sides */
.sides-intro{position:absolute;left:39px;top:62px;font-family:"Arvo",serif;color:var(--blue);line-height:1.05}
.sides-intro .sm{font-size:8.5px}
.sides-intro .lg{font-size:13px;font-weight:700}
.script{position:absolute;font-family:"Monsieur La Doulaise",cursive;color:var(--blue)}
.lados{left:222px;top:8px;font-size:64px;line-height:1}
.script-sub{position:absolute;font-family:"Oswald",sans-serif;color:var(--blue);font-size:10px;letter-spacing:.8px}
.sides-list{position:absolute;left:39px;top:115px;width:319px}
.sides-list .item{margin-bottom:0}
.sides-list .item-head{color:var(--rust);font-size:11.5px;line-height:13.6px}
.sides-list .price{color:var(--rust);font-size:9.5px}
.sides-list .desc{font-size:10px;line-height:12px}
.beans-art{position:absolute;left:190px;top:163px;width:106px;height:110px;border-radius:40% 40% 20% 20%;background:linear-gradient(160deg,#b8d3eb,#8fb7dc);opacity:.7}

.kids{left:26px;top:312px;width:335px;height:170px}
.kids-head{height:60px;border-bottom:1.5px solid var(--frame);padding:10px 0 0 14px}
.kids-head h2{font-family:"Arvo",serif;font-weight:700;color:var(--blue);font-size:22px;line-height:1}
.kids-head p{font-family:"Oswald",sans-serif;color:var(--blue);font-size:10px;letter-spacing:.6px;margin-top:2px}
.kids .list{padding:9px 20px 0 13px}
.kids .item-head{color:var(--rust);font-size:11.5px}
.kids .price{color:var(--rust);font-size:9.5px}
.kids .desc{font-size:10px;line-height:12px}
.kids .item{margin-bottom:2px}

.dessert{position:absolute}
.dessert .dish-title{font-size:14px;line-height:14.5px}
.dessert .amt{font-size:11px;margin:4px 0 3px}
.dessert .small-text{font-size:10px;line-height:11.8px}
.churro{left:40px;top:516px;width:150px}
.churro-art{position:absolute;left:85px;top:506px;width:92px;height:130px;background:linear-gradient(150deg,#9cc2e4,#6fa5d4);opacity:.35;border-radius:6px;transform:rotate(-14deg)}
.fine{font-size:6.5px;font-weight:700;margin-top:2px;text-transform:uppercase}
.postre{left:204px;top:505px;font-size:58px;line-height:1}
.helado{left:40px;top:650px;width:165px}
.local{left:217px;top:650px;width:150px}
</style>
</head>
<body>
<main class="menu">

  <section class="panel panel--left">
    <div class="framed appetizers">
      <h1 class="section-title">MERIENDAS</h1>
      <p class="section-sub">Appetizers</p>
      <div class="list">
        <div class="item"><div class="item-head"><span>Island Ceviche</span><span class="price">18.00</span></div>
          <p class="desc">Ono fish marinated in fresh lime juice and tossed with onion, cilantro and tomato</p></div>
        <div class="item"><div class="item-head"><span>Kalua Pork Nachos</span><span class="price">15.00</span></div>
          <p class="desc">Freshly made local tortilla chips, topped with Kalua pork, black beans, cheese, guacamole, sour cream and salsa</p></div>
        <div class="item"><div class="item-head"><span>Locally Made Tortilla Chips</span><span></span></div>
          <p class="desc">Thick sliced quiche piled high with fresh garden vegetables and served with a house salad -- choose from ham, bacon, or vegetable</p>
          <div class="opt"><span>Guacamole and Traditional Salsa</span><span class="price">14.00</span></div>
          <div class="opt"><span>Traditional and Grilled Salsa</span><span class="price">12.00</span></div></div>
        <div class="item"><div class="item-head"><span>Quesadilla</span><span class="price">10.00</span></div>
          <p class="desc">Large flour tortilla filled with a blend of Mild cheddar and Monterey Jack cheese. Served with a side of our traditional salsa</p>
          <div class="opt"><span>Add Grilled Chicken</span><span class="price">12.00</span></div>
          <div class="opt"><span>Add Carne Asada</span><span class="price">14.00</span></div></div>
        <div class="item"><div class="item-head"><span>Solvaro Taquitos</span><span class="price">12.00</span></div>
          <p class="desc">(3) rolled crispy tacos, filled with shredded chicken and topped with lettuce, cheese, guacamole and pico de gallo</p></div>
      </div>
    </div>

    <div class="framed soup-salad">
      <div class="band">Sopa y Ensalada (Soup an Salad)</div>
      <div class="cols">
        <div class="soup-col">
          <h3 class="dish-title">Solvaro Tortilla Soup</h3>
          <p class="small-text soup-text">Traditional chicken tortilla soup, topped with a dollop of sour cream, cilantro and tortilla strips</p>
          <div class="soup-art" role="img" aria-label="Illustration of a bowl of tortilla soup"></div>
          <div class="sizes"><div><span>CUP</span><span>7.00</span></div><div><span>BOWL</span><span>10.00</span></div></div>
        </div>
        <div class="salad-col">
          <h3 class="dish-title">Caesar's Tijuana Salad</h3>
          <p class="salad-price">14.00</p>
          <p class="small-text">fresh romaine topped with grilled chicken and tortilla strips. Our creamy ceasar dressing served on the side</p>
        </div>
      </div>
      <div class="suprema">
        <h3 class="dish-title">Fajita Suprema Salad</h3>
        <p class="small-text">Large flour tostada salad bowl, filled with fresh crisp greens, your choice of meat and topped with guacamole, sour cream and pico de gallo</p>
        <div class="opt"><span>Fajita Grilled Chicken and Veggies</span><span class="price">18.00</span></div>
        <div class="opt"><span>Fajita GSteak and Veggies</span><span class="price">20.00</span></div>
      </div>
    </div>
  </section>

  <section class="panel panel--specials">
    <div class="framed specials">
      <h1 class="section-title">SOLVARO'S ESPECIALES</h1>
      <p class="section-sub">Specials</p>
      <div class="list">
        <div class="item"><div class="item-head"><span>Sizzling Fajitas</span><span></span></div>
          <p class="desc">Sizzling platter with strips of onions and bell pepper, and your choice of meat. Served with warm tortillas, and your choice of beans and rice</p>
          <div class="opt"><span>Fajita Grilled Chicken and Veggies</span><span class="price">22.00</span></div>
          <div class="opt"><span>Fajita Grilled Steak and Veggies</span><span class="price">24.00</span></div>
          <div class="opt"><span>Fajita Grilled Shrimp and Veggies</span><span class="price">26.00</span></div>
          <div class="opt"><span>Trio includes chicken, steak, shrimp and veggies</span><span class="price">28.00</span></div></div>
        <div class="item"><div class="item-head"><span>Tacos Dorado</span><span></span></div>
          <p class="desc">Two classic hard shell tacos, served with your choice of meat, topped with lettuce, cheese and tomato, Served with a side of traditional salsa</p>
          <div class="opt"><span>Shredded Chicken</span><span class="price">12.00</span></div>
          <div class="opt"><span>Shredded Beef</span><span class="price">14.00</span></div></div>
        <div class="item"><div class="item-head"><span>Street Tacos</span><span></span></div>
          <p class="desc">(3) California style soft tacos topped with your choice of meat and white onion and cilantro. Served with a side of traditional salsa</p>
          <div class="opt"><span>Black Bean and Potato</span><span class="price">10.00</span></div>
          <div class="opt"><span>Grilled Chicken</span><span class="price">12.00</span></div>
          <div class="opt"><span>Carne Asada</span><span class="price">14.00</span></div></div>
        <div class="item"><div class="item-head"><span>Birria Tacos</span><span class="price">16.00</span></div>
          <p class="desc">(3) corn tortillas stuffed with shredded beef, cheese, onion and cilantro. Served with a side of dipping broth, traditional salsa and lime wedges</p></div>
        <div class="item"><div class="item-head"><span>Grilled Ono Tacos</span><span class="price">16.00</span></div>
          <p class="desc">two soft corn tortillas filled with grilled Ono, shredded cabbage and topped with cilantro lime crema. Served with a side of traditional salsa and lime wedges</p></div>
        <div class="item"><div class="item-head"><span>Aloha Combination</span><span class="price">16.00</span></div>
          <p class="desc">Includes a shredded beef Taco Dorado, cheese enchilada, rice and refried beans. Served with a side of traditional salsa</p></div>
        <div class="item"><div class="item-head"><span>Macho Solvaro Burrito</span><span class="price">16.00</span></div>
          <p class="desc">Filled with carne asada, beans De La Olla, rice, onions, cilantro and guacamole. Served with a side of traditional salsa.</p></div>
        <div class="item"><div class="item-head"><span>Kalua Carnitas Platter</span><span class="price">16.00</span></div>
          <p class="desc">Slow cooked pork, rice, Oaxaca black beans, and tortillas. Served with a side of guacamole, sour cream and traditional salsa.</p></div>
        <div class="item"><div class="item-head"><span>Surf &amp; Turf</span><span class="price">16.00</span></div>
          <p class="desc">Bacon wrapped shrimp and carne asada, served with beans De La Olla, rice and warm tortillas. Served with your choice of spicy Diablo or garlic butter sauce.</p></div>
        <div class="item"><div class="item-head"><span>Camarones Diablo</span><span class="price">16.00</span></div>
          <p class="desc">Sauteed Shrimp in a Spicy Diablo sauce, beans De La Olla, rice and warm tortillas. Served with a side of sour cream. traditional salsa.</p></div>
      </div>
    </div>
  </section>

  <section class="panel panel--right">
    <div class="sides-intro">
      <div class="sm">ENJOY YOUR CHOICE OF</div>
      <div class="lg">THREE STYLE OF BEANS</div>
      <div class="sm">MADE FRESH DAILY!</div>
    </div>
    <h1 class="script lados">Lados</h1>
    <p class="script-sub" style="left:292px;top:72px">SIDES</p>
    <div class="beans-art" role="img" aria-label="Illustration of a bowl of guacamole with tortilla chips"></div>
    <div class="sides-list">
      <div class="item"><div class="item-head"><span>Traditional Refried Beans</span><span class="price">16.00</span></div></div>
      <div class="item"><div class="item-head"><span>Beans De La Olla</span><span class="price">16.00</span></div>
        <p class="desc">Whole pinto beans, tomato, onion, cilantro and spices</p></div>
      <div class="item"><div class="item-head"><span>Oaxaca Black Beans</span><span class="price">16.00</span></div>
        <p class="desc">Whole black beans with onion and spices</p></div>
      <div class="item"><div class="item-head"><span>Mexican Rice</span><span class="price">16.00</span></div>
        <p class="desc">Special family secret!</p></div>
      <div class="item"><div class="item-head"><span>Guacamole- Ramikin</span><span class="price">16.00</span></div></div>
      <div class="item"><div class="item-head"><span>Sour Cream</span><span class="price">16.00</span></div></div>
      <div class="item"><div class="item-head"><span>Tortillas</span><span class="price">16.00</span></div>
        <p class="desc">(3) corn or flour</p></div>
    </div>

    <div class="framed kids">
      <div class="kids-head"><h2>KEIKE MENU</h2><p>AGE 10 AND UNDER</p></div>
      <div class="list">
        <div class="item"><div class="item-head"><span>Taquitos</span><span class="price">16.00</span></div>
          <p class="desc">Two rolled chaquita chicken tacos, served with refried beans and rice</p></div>
        <div class="item"><div class="item-head"><span>Cheese Quesadilla</span><span class="price">16.00</span></div>
          <p class="desc">Chaquita quesadilla, served with refried beans and rice</p></div>
        <div class="item"><div class="item-head"><span>Keiki Burrito</span><span class="price">16.00</span></div>
          <p class="desc">Flour tortilla filled with refried beans and cheese</p></div>
      </div>
    </div>

    <div class="churro-art" role="img" aria-label="Illustration of churros"></div>
    <div class="dessert churro">
      <h3 class="dish-title">Churro<br>Deliciosa</h3>
      <p class="amt">14.00</p>
      <p class="small-text">Your own cart filled with "Mexican Doughnuts" fried and rolled in cinnamon sugar. Served with chocolate, carmel and strawberry sauce.</p>
      <p class="fine">Add one scoop of vanilla ice cream (3.00)</p>
    </div>
    <h2 class="script postre">El Postre's</h2>
    <p class="script-sub" style="left:310px;top:597px">DESSERTS</p>
    <div class="dessert helado">
      <h3 class="dish-title">Solvaro's Helado<br>y Papas Frita</h3>
      <p class="amt">12.00</p>
      <p class="small-text">one scoop of local vanilla bean ice cream. Served with our homemade tortilla chips sprinkled with cinnamon and sugar</p>
    </div>
    <div class="dessert local">
      <h3 class="dish-title">Local<br>Dessert</h3>
      <p class="amt">10.00</p>
      <p class="small-text">Unique every day. Ask your server for more details</p>
    </div>
  </section>

</main>
</body>
</html>
```